Vantor Law Group Bus Card Design

We need a business card for our law firm that specializes in intellectual property law (patents, trademarks, copyrights). We are called The Vantor Law Group. We have a globe logo (attached) that is currently the back of our card. We like the back, but aren't married to it. I will also attach the front side of what we use now. The black background looks bad/cheap. We want something that looks sharp and modern. Thank you.

Law Firm

```html
<!DOCTYPE html>
<html lang="en">
<head>
<meta charset="utf-8">
<title>Vantor Law Group Business Card</title>
<link rel="stylesheet" href="https://fonts.googleapis.com/css2?family=Open+Sans:wght@400;600;700&display=swap">
<style>
  :root {
    --stage: #3b3e43;
    --card-blue: #5fa7dc;
    --card-white: #f7f7f8;
    --ink: #2f3033;
    --ink-soft: #3c3d40;
    --accent: #4b9ad6;
    --icon-ink: #1f2a36;
    --rule: #c9cbd0;
    --deco-start: #c9d9ea;
    --deco-end: #f7f7f8;
  }
  * { box-sizing: border-box; margin: 0; padding: 0; }
  html, body { width: 1200px; height: 864px; overflow: hidden; }
  body {
    background: var(--stage);
    font-family: "Open Sans", Arial, sans-serif;
    position: relative;
  }
  .card {
    position: absolute;
    width: 560px;
    height: 320px;
    border-radius: 4px;
    overflow: hidden;
  }
  .card-back {
    left: 250px; top: 70px;
    background: var(--card-blue);
    display: flex; flex-direction: column; align-items: center; justify-content: center;
    text-align: center;
  }
  .brand { display: flex; align-items: center; gap: 10px; }
  .brand-dot { width: 26px; height: 26px; border-radius: 50%; background: #ffffff; }
  .brand-name {
    font-weight: 700; font-size: 21px; color: var(--ink);
    font-variant: small-caps; letter-spacing: 0.5px;
  }
  .tagline {
    margin-top: 6px; font-size: 12px; font-weight: 700; color: var(--ink);
    font-variant: small-caps; letter-spacing: 0.6px;
  }
  .back-site {
    margin-top: 26px; font-size: 12px; font-weight: 700; color: var(--ink);
    font-variant: small-caps; letter-spacing: 0.5px;
  }
  .card-front { left: 200px; top: 450px; background: var(--card-white); }
  .front-deco {
    position: absolute; left: 0; top: 0; width: 250px; height: 320px;
    background: linear-gradient(90deg, var(--deco-start), var(--deco-end));
  }
  .person { position: absolute; left: 36px; top: 96px; }
  .person-name { font-size: 27px; font-weight: 600; color: var(--ink-soft); line-height: 1.1; }
  .person-title { font-size: 15px; color: var(--accent); }
  .front-brand { position: absolute; right: 36px; top: 70px; text-align: left; }
  .front-brand .brand-name { font-size: 19px; }
  .front-brand .brand-dot { background: var(--accent); }
  .front-brand .tagline { font-size: 11px; padding-left: 36px; }
  .rule {
    position: absolute; left: 250px; right: 36px; top: 160px;
    height: 1px; background: var(--rule);
  }
  .contacts {
    position: absolute; right: 36px; top: 178px;
    list-style: none; text-align: right;
  }
  .contacts li {
    display: flex; justify-content: flex-end; align-items: center; gap: 10px;
    font-size: 16px; color: var(--ink-soft); line-height: 24px;
  }
  .icon {
    width: 17px; height: 17px; background: var(--accent); border-radius: 2px;
    display: inline-flex; align-items: center; justify-content: center;
  }
  .icon svg { width: 11px; height: 11px; fill: var(--icon-ink); }
</style>
</head>
<body>
  <section class="card card-back">
    <div class="brand">
      <span class="brand-dot"></span>
      <span class="brand-name">The Vantor Law Group</span>
    </div>
    <p class="tagline">Patents | Copyrights | Trademarks</p>
    <p class="back-site">www.VantorLaw.com</p>
  </section>

  <section class="card card-front">
    <div class="front-deco" role="img" aria-label="Faint pale blue circuit-board globe decoration"></div>
    <div class="person">
      <p class="person-name">Daniel Reyes</p>
      <p class="person-title">Managing Director</p>
    </div>
    <div class="front-brand">
      <div class="brand">
        <span class="brand-dot"></span>
        <span class="brand-name">The Vantor Law Group</span>
      </div>
      <p class="tagline">Patents | Copyrights | Trademarks</p>
    </div>
    <div class="rule"></div>
    <ul class="contacts">
      <li>044-456-7890 <span class="icon"><svg viewBox="0 0 12 12"><path d="M1 4c0-2 2-3 5-3s5 1 5 3l-2 1-1-1H4L3 5zM2 6h8l1 5H1z"/></svg></span></li>
      <li>123-456-7890 <span class="icon"><svg viewBox="0 0 12 12"><path d="M3 1h5v3H3zM1 4h10v7H1zM3 6h2v1H3zm4 0h2v1H7zM3 8h2v1H3zm4 0h2v1H7z"/></svg></span></li>
      <li>123-456-7890 <span class="icon"><svg viewBox="0 0 12 12"><path d="M3 0h6v12H3zm1 1v8h4V1zm1.5 9h1v1h-1z"/></svg></span></li>
      <li>info@youremail.com <span class="icon"><svg viewBox="0 0 12 12"><path d="M1 2h10v8H1zm1 1l4 3 4-3z"/></svg></span></li>
      <li>www.website.com <span class="icon"><svg viewBox="0 0 12 12"><path d="M2 7l3-3 1 1-3 3 1 1 3-3 1 1-3 3c-1 1-2 1-3 0s-1-2 0-3zm8-2L7 8 6 7l3-3-1-1-3 3-1-1 3-3c1-1 2-1 3 0s1 2 0 3z"/></svg></span></li>
    </ul>
  </section>
</body>
</html>
```